Dr. Marisa Tellen Medical/Chiropractic Business Card

Dr. Tellen is a chiropractor and will require a business card that she uses every single day to book appointments on the back side of the card. Currently the office name goes by Dr. Marisa Tellen. The chiropractic profession is based on the diagnosis and manipulative treatment of misalignments of the joints, especially those of the spinal column, which are held to cause other disorders by affecting the nerves, muscles, and organs. Dr. Marisa Tellen is looking for a contemporary and minimalistic design.

Industry/Entity Type

Medical

Contact Information for Business Card

Name: Dr. Marisa Tellen; Address: 748 Ashcombe Rd North, London, ON N5R 2K9; Phone Number: 519.672.4193; Fax: 519.681.2054; email: marisa.tellen@brevanmail.com

Requirements
Must have
• ability to write multiple appointments date/time on the back of card

```html
<!DOCTYPE html>
<html lang="en">
<head>
<meta charset="utf-8">
<title>Dr. Marisa Tellen – Business Card</title>
<link rel="stylesheet" href="https://fonts.googleapis.com/css2?family=Montserrat:wght@400;500;600;700&display=swap">
<style>
  :root {
    --bg: #2b2b2d;
    --card-white: #ffffff;
    --navy: #1c1a3d;
    --ink: #1c1a3d;
    --text-light: #ffffff;
  }
  * { box-sizing: border-box; margin: 0; padding: 0; }
  html, body { width: 1200px; height: 900px; overflow: hidden; }
  body {
    background: var(--bg);
    font-family: "Montserrat", Arial, sans-serif;
    position: relative;
  }
  .card {
    position: absolute;
    width: 700px;
    height: 400px;
    box-shadow: 0 10px 24px rgba(0,0,0,0.45);
  }

  /* Back: appointment card */
  .card-back {
    left: 110px; top: 40px;
    background: var(--card-white);
    color: var(--ink);
  }
  .appt-title {
    position: absolute; left: 150px; top: 44px;
    font-weight: 700; font-size: 15px; letter-spacing: 1.5px;
  }
  .appt-time {
    position: absolute; left: 430px; top: 44px;
    font-weight: 700; font-size: 15px; letter-spacing: 1.5px;
  }
  .appt-date {
    position: absolute; left: 40px; top: 110px;
    font-weight: 700; font-size: 15px; letter-spacing: 1.5px;
  }
  .appt-lines { position: absolute; left: 0; top: 0; }
  .appt-note {
    position: absolute; left: 40px; bottom: 28px;
    font-size: 15px; font-weight: 400; letter-spacing: 0.3px;
  }

  /* Front: identity card */
  .card-front {
    left: 390px; top: 470px;
    background: var(--navy);
    color: var(--text-light);
  }
  .brand-square {
    position: absolute; right: 0; top: 74px;
    width: 30px; height: 30px; background: var(--card-white);
  }
  .doctor-name {
    position: absolute; right: 42px; top: 72px;
    font-weight: 700; font-size: 26px; letter-spacing: 1px;
  }
  .doctor-title {
    position: absolute; right: 42px; top: 106px;
    font-weight: 400; font-size: 14px; letter-spacing: 1.5px;
  }
  .title-rule {
    position: absolute; right: 178px; top: 116px;
    width: 150px; height: 1.5px; background: var(--text-light);
  }
  .name-rule {
    position: absolute; left: 40px; top: 138px;
    width: 370px; height: 1.5px; background: var(--text-light);
  }
  .address {
    position: absolute; right: 42px; top: 148px;
    text-align: right; font-size: 14px; line-height: 1.35; letter-spacing: 0.5px;
  }
  .contact-rule {
    position: absolute; left: 40px; top: 290px;
    width: 200px; height: 1.5px; background: var(--text-light);
  }
  .contact-list {
    position: absolute; left: 40px; top: 302px;
    list-style: none; font-size: 15px; line-height: 1.45; letter-spacing: 0.4px;
  }
  .contact-list li { display: flex; align-items: center; gap: 10px; }
  .contact-list svg { width: 13px; height: 13px; fill: var(--text-light); }
</style>
</head>
<body>

<section class="card card-back" aria-label="Appointment side">
  <svg class="appt-lines" width="700" height="400" viewBox="0 0 700 400" aria-hidden="true">
    <g stroke="#1c1a3d" stroke-width="1.6">
      <line x1="40" y1="70" x2="330" y2="70"/>
      <line x1="40" y1="132" x2="330" y2="132"/>
      <line x1="40" y1="172" x2="330" y2="172"/>
      <line x1="40" y1="212" x2="330" y2="212"/>
      <line x1="40" y1="252" x2="330" y2="252"/>
      <line x1="40" y1="292" x2="330" y2="292"/>
      <line x1="380" y1="70" x2="660" y2="70"/>
      <line x1="380" y1="112" x2="660" y2="112"/>
      <line x1="380" y1="152" x2="660" y2="152"/>
      <line x1="380" y1="192" x2="660" y2="192"/>
      <line x1="380" y1="232" x2="660" y2="232"/>
      <line x1="380" y1="272" x2="660" y2="272"/>
      <line x1="380" y1="312" x2="660" y2="312"/>
    </g>
  </svg>
  <h2 class="appt-title">APPOINTMENTS</h2>
  <span class="appt-time">TIME</span>
  <span class="appt-date">DATE</span>
  <p class="appt-note">If you are unable to make your appointment, please call us to reschedule</p>
</section>

<section class="card card-front" aria-label="Contact side">
  <span class="brand-square"></span>
  <h1 class="doctor-name">DR. MARISA TELLEN</h1>
  <span class="title-rule"></span>
  <p class="doctor-title">CHIROPRACTOR</p>
  <span class="name-rule"></span>
  <address class="address" style="font-style:normal">748 Ashcombe Rd North,<br>London, ON N5R 2K9</address>
  <span class="contact-rule"></span>
  <ul class="contact-list">
    <li>
      <svg viewBox="0 0 24 24" aria-label="Phone"><path d="M6.6 10.8a15 15 0 0 0 6.6 6.6l2.2-2.2c.3-.3.7-.4 1-.2 1.1.4 2.3.6 3.6.6.6 0 1 .4 1 1V20c0 .6-.4 1-1 1A17 17 0 0 1 3 4c0-.6.4-1 1-1h3.5c.6 0 1 .4 1 1 0 1.3.2 2.5.6 3.6.1.3 0 .7-.2 1z"/></svg>
      519.672.4193
    </li>
    <li>
      <svg viewBox="0 0 24 24" aria-label="Fax"><path d="M6 2h10v5H6zM4 9h16a2 2 0 0 1 2 2v7h-4v4H6v-4H2v-7a2 2 0 0 1 2-2zm4 8v3h8v-3z"/></svg>
      519.681.2054
    </li>
    <li>
      <svg viewBox="0 0 24 24" aria-label="Email"><path d="M2 5h20v14H2zm2 2v.5l8 5 8-5V7zm0 2.8V17h16V9.8l-8 5z"/></svg>
      marisa.tellen@brevanmail.com
    </li>
  </ul>
</section>

</body>
</html>
```